Brightpath Letterhead

We would like a letterhead for our company. I have uploaded our logo.

Brightpath Ridge Consulting
1450 W Corliss Ave Ste 310
Maple Crest, TX 76120
833-517-2906

```html
<!DOCTYPE html>
<html lang="en">
<head>
<meta charset="utf-8">
<title>Brightpath Ridge Consulting — Letterhead</title>
<link rel="stylesheet" href="https://fonts.googleapis.com/css2?family=Josefin+Sans:wght@600&family=Barlow:wght@400&display=swap">
<style>
  :root {
    --green: #6cc59a;
    --teal: #17606b;
    --navy: #0d1a3e;
    --mint-soft: #d8ede1;
    --trim: #bfe3dc;
    --backdrop: #eceef0;
    --paper: #ffffff;
  }
  * { margin: 0; padding: 0; box-sizing: border-box; }
  html, body {
    width: 1200px;
    height: 2462px;
    overflow: hidden;
    background: var(--backdrop);
  }
  .letterhead {
    position: absolute;
    left: 0;
    top: 400px;
    width: 1200px;
    height: 1663px;
    background: var(--paper);
    overflow: hidden;
  }
  .edge-band {
    position: absolute;
    left: 0;
    width: 53px;
  }
  .edge-band--green { top: 0; height: 555px; background: var(--green); }
  .edge-band--teal { top: 555px; height: 553px; background: var(--teal); }
  .edge-band--navy { top: 1108px; height: 555px; background: var(--navy); }

  .trim-line {
    position: absolute;
    left: 53px;
    top: 33px;
    width: 1112px;
    height: 1608px;
    border: 1px solid var(--trim);
    border-left: none;
  }
  .crop-mark { position: absolute; background: #9aa3a8; }
  .crop-mark--v { left: 1165px; top: 0; width: 1px; height: 24px; }
  .crop-mark--h { left: 1172px; top: 33px; width: 28px; height: 1px; }

  .brand {
    position: absolute;
    left: 125px;
    top: 108px;
    display: flex;
    align-items: center;
    gap: 22px;
  }
  .brand-dot {
    width: 78px;
    height: 78px;
    border-radius: 50%;
    background: var(--teal);
    flex: none;
  }
  .brand-name {
    font-family: "Josefin Sans", sans-serif;
    font-weight: 600;
    color: var(--teal);
    font-size: 44px;
    line-height: 1.05;
    letter-spacing: 3px;
    text-transform: uppercase;
  }
  .brand-name span { display: block; }

  .backdrop-mark {
    position: absolute;
    left: 105px;
    top: 895px;
    width: 500px;
    height: 500px;
    border-radius: 50%;
    background: var(--mint-soft);
  }

  .contact {
    position: absolute;
    right: 120px;
    top: 1330px;
    list-style: none;
    font-family: "Barlow", sans-serif;
    font-weight: 400;
    font-size: 20px;
    color: var(--teal);
    letter-spacing: 0.3px;
  }
  .contact-item {
    display: flex;
    align-items: flex-start;
    justify-content: flex-end;
    gap: 18px;
    margin-bottom: 17px;
    text-align: right;
  }
  .contact-item:nth-child(3) { margin-bottom: 20px; }
  .contact-text { line-height: 30px; }
  .contact-text span { display: block; line-height: 36px; }
  .contact-text span:first-child { line-height: 30px; }
  .contact-icon { width: 28px; height: 28px; flex: none; margin-top: 1px; }
</style>
</head>
<body>
  <main class="letterhead">
    <div class="edge-band edge-band--green"></div>
    <div class="edge-band edge-band--teal"></div>
    <div class="edge-band edge-band--navy"></div>
    <div class="trim-line"></div>
    <div class="crop-mark crop-mark--v"></div>
    <div class="crop-mark crop-mark--h"></div>

    <header class="brand">
      <div class="brand-dot"></div>
      <h1 class="brand-name"><span>Brightpath Ridge</span><span>Consulting</span></h1>
    </header>

    <div class="backdrop-mark"></div>

    <ul class="contact">
      <li class="contact-item">
        <span class="contact-text">833-517-2906</span>
        <svg class="contact-icon" viewBox="0 0 28 28" fill="none" stroke="#17606b" stroke-width="2">
          <circle cx="14" cy="14" r="12.5"/>
          <path d="M10 8.5c-1.5 1-1.8 3 -0.6 5.4 1.3 2.6 3.3 4.6 5.3 5.6 2 1 3.6.6 4.5-.7l-2.2-2.2-1.8 1c-1.4-.8-2.6-2-3.4-3.5l1-1.8z" stroke-linejoin="round"/>
        </svg>
      </li>
      <li class="contact-item">
        <span class="contact-text">contact@brightpathridge.com</span>
        <svg class="contact-icon" viewBox="0 0 28 28" fill="none" stroke="#17606b" stroke-width="2">
          <circle cx="14" cy="14" r="12.5"/>
          <rect x="8" y="9.5" width="12" height="9" rx="1" fill="#17606b" stroke="none"/>
          <path d="M8.5 10.5l5.5 4.5 5.5-4.5" stroke="#fff" stroke-width="1.4"/>
        </svg>
      </li>
      <li class="contact-item">
        <span class="contact-text">brightpathridge.com</span>
        <svg class="contact-icon" viewBox="0 0 28 28" fill="none" stroke="#17606b" stroke-width="2">
          <circle cx="14" cy="14" r="12.5"/>
          <ellipse cx="14" cy="14" rx="4.5" ry="12"/>
          <path d="M2 14h24M4 8h20M4 20h20"/>
        </svg>
      </li>
      <li class="contact-item">
        <span class="contact-text"><span>1450 W Corliss Ave Ste 310</span><span>Maple Crest, TX 76120</span></span>
        <svg class="contact-icon" viewBox="0 0 28 28" fill="none" stroke="#17606b" stroke-width="2">
          <circle cx="14" cy="14" r="12.5"/>
          <path d="M14 22c-3.5-4-5.5-7-5.5-9.5a5.5 5.5 0 0 1 11 0c0 2.5-2 5.5-5.5 9.5z" stroke-linejoin="round"/>
          <circle cx="14" cy="12.5" r="2"/>
        </svg>
      </li>
    </ul>
  </main>
</body>
</html>
```